Maison Corvel

I am actually making my own traditional french food.
Everything is homemade with passion.
I make differente terrines, jams, macaroons, rillettes and much more
I do as well cocktail party and catering
Updates

Hello everyone,

On the business card I would like to see appear if it's possible these following informations: traditional french food, cocktail party and catering.

Industry/Entity Type

Catering

```html
<!DOCTYPE html>
<html lang="fr">
<head>
<meta charset="utf-8">
<title>Maison Corvel — Business Card</title>
<link rel="stylesheet" href="https://fonts.googleapis.com/css2?family=Bitter:wght@700&family=PT+Sans:wght@400;700&display=swap">
<style>
  :root {
    --backdrop: #e9e6e1;
    --card-white: #ffffff;
    --ink: #231f20;
    --accent-red: #c1272d;
    --navy: #2e3192;
    --on-navy: #ffffff;
  }
  * { box-sizing: border-box; margin: 0; padding: 0; }
  html, body {
    width: 1162px;
    height: 1200px;
    overflow: hidden;
    background: var(--backdrop);
  }
  .stage {
    width: 1162px;
    height: 1200px;
    display: flex;
    flex-direction: column;
    align-items: center;
    justify-content: space-evenly;
  }
  .card {
    position: relative;
    width: 950px;
    height: 540px;
    box-shadow: 0 4px 14px rgba(0,0,0,0.18);
  }

  /* Front */
  .card--front {
    background: var(--card-white);
    border-top: 13px solid var(--ink);
    border-bottom: 13px solid var(--ink);
  }
  .brand {
    position: absolute;
    top: 170px;
    left: 0;
    right: 0;
    display: flex;
    justify-content: center;
    align-items: center;
    gap: 22px;
  }
  .brand__dot {
    width: 46px;
    height: 46px;
    border-radius: 50%;
    background: var(--accent-red);
  }
  .brand__name {
    font-family: "Bitter", Georgia, serif;
    font-weight: 700;
    font-size: 64px;
    line-height: 1.1;
    letter-spacing: 2px;
    text-transform: uppercase;
    color: var(--ink);
  }
  .services {
    position: absolute;
    top: 262px;
    left: 0;
    right: 0;
    text-align: center;
    font-family: "PT Sans", Arial, sans-serif;
    font-weight: 700;
    font-size: 20px;
    letter-spacing: 3px;
    text-transform: uppercase;
    color: var(--ink);
  }
  .services__sep { color: var(--accent-red); margin: 0 10px; }
  .holder {
    position: absolute;
    top: 362px;
    left: 0;
    right: 0;
    text-align: center;
    font-family: "Bitter", Georgia, serif;
    font-weight: 700;
    font-size: 34px;
    color: var(--accent-red);
  }
  .contact {
    position: absolute;
    top: 428px;
    left: 0;
    right: 0;
    display: flex;
    justify-content: center;
    align-items: center;
    gap: 12px;
    font-family: "PT Sans", Arial, sans-serif;
    font-size: 24px;
    color: var(--ink);
  }
  .contact__item { display: flex; align-items: center; gap: 6px; }
  .contact__icon { width: 20px; height: 20px; fill: var(--accent-red); }
  .contact__divider {
    width: 1px;
    height: 30px;
    background: var(--ink);
    margin: 0 6px;
  }

  /* Back */
  .card--back { background: var(--navy); }
  .back-brand {
    position: absolute;
    top: 220px;
    left: 0;
    right: 0;
    display: flex;
    justify-content: center;
    align-items: center;
    gap: 24px;
  }
  .back-brand__dot {
    width: 52px;
    height: 52px;
    border-radius: 50%;
    background: var(--on-navy);
  }
  .back-brand__name {
    font-family: "Bitter", Georgia, serif;
    font-weight: 700;
    font-size: 72px;
    line-height: 1.1;
    letter-spacing: 2px;
    text-transform: uppercase;
    color: var(--on-navy);
  }
  .website {
    position: absolute;
    top: 462px;
    left: 0;
    right: 0;
    text-align: center;
    font-family: "PT Sans", Arial, sans-serif;
    font-size: 30px;
    letter-spacing: 2px;
    color: var(--on-navy);
  }
</style>
</head>
<body>
<main class="stage">
  <section class="card card--front" aria-label="Card front">
    <div class="brand">
      <span class="brand__dot" aria-hidden="true"></span>
      <span class="brand__name">Maison Corvel</span>
    </div>
    <p class="services">Traditional French Food<span class="services__sep">·</span>Cocktail Party<span class="services__sep">·</span>Catering</p>
    <p class="holder">Étienne Valmont</p>
    <div class="contact">
      <span class="contact__item">
        <svg class="contact__icon" viewBox="0 0 24 24" aria-hidden="true"><path d="M6.6 10.8a15.1 15.1 0 0 0 6.6 6.6l2.2-2.2a1 1 0 0 1 1-.25 11.4 11.4 0 0 0 3.6.57 1 1 0 0 1 1 1V20a1 1 0 0 1-1 1A17 17 0 0 1 3 4a1 1 0 0 1 1-1h3.5a1 1 0 0 1 1 1c0 1.25.2 2.45.57 3.57a1 1 0 0 1-.25 1z"/></svg>
        041-5230-776
      </span>
      <span class="contact__item">
        <svg class="contact__icon" viewBox="0 0 24 24" aria-hidden="true"><path d="M3 6h18v12H3z M3 6l9 7 9-7" fill="none" stroke="#c1272d" stroke-width="2.4"/></svg>
        etienne.v@corvel.fr
      </span>
      <span class="contact__divider" aria-hidden="true"></span>
      <span class="contact__item">ABN: 98312460751</span>
    </div>
  </section>

  <section class="card card--back" aria-label="Card back">
    <div class="back-brand">
      <span class="back-brand__dot" aria-hidden="true"></span>
      <span class="back-brand__name">Maison Corvel</span>
    </div>
    <p class="website">www.maisoncorvel.com</p>
  </section>
</main>
</body>
</html>
```